Lantern - Web Design Project

We are seeking to have our website redesigned. Our current webpage is rather dated looking www.lantern-outcomes.com We will be utilizing similar content to explain our services as what is in the website now. We do not see it at a retail portal but rather a website for those inquiring about our services as a reference check so to speak.

We wish to have a look that is considered clean, fresh, contemporary and contains a business savvy vibe.

We prefer isolated white background and also wish to retain the integrity of our Logo and colour scheme.

We are looking for something that doesnt look like it was designed at home on sitemoose. We are hoping to find something that looks like it would reside on a tablet.
Updates

Hello designers!

We apologize for our tardiness as we have been quite preoccupied. We will be extending our invites to the end of January!

Hello All,

Please review our offer once again for updated requirements.  We are hoping to accept a design by months end.

Lantern

Target Market(s)

Business to business clients and Large manufacturers

Industry/Entity Type

Retail

Requirements
Must have
• Existing Logo

There must be an area dedicated to an intro video that will be incorporated on our landing page.

We require design of the other pages as well not only the landing page.

```html
<!DOCTYPE html>
<html lang="en">
<head>
<meta charset="utf-8">
<title>Lantern Performance Group</title>
<link href="https://fonts.googleapis.com/css2?family=Arimo:ital,wght@0,400;0,700;1,400&display=swap" rel="stylesheet">
<style>
:root{
  --red:#e3141b;
  --red-dark:#7c1414;
  --charcoal:#5a5555;
  --text:#666;
  --heading:#777;
  --navy:#0f3a62;
  --footer:#dde0e8;
  --rule:#d6d6d6;
}
*{margin:0;padding:0;box-sizing:border-box}
html,body{width:1200px;height:1000px;overflow:hidden;background:#fff}
body{font-family:"Arimo",Helvetica,Arial,sans-serif;color:var(--text);position:relative}
.abs{position:absolute}
.top-strip{left:0;top:0;width:1200px;height:10px;background:var(--charcoal)}
.top-strip::after{content:"";position:absolute;left:120px;width:960px;height:10px;background:var(--red)}
.header{left:0;top:10px;width:1200px;height:110px;background:#fff}
.brand{left:119px;top:30px;display:flex;align-items:center;gap:8px;font-size:46px;color:var(--charcoal);letter-spacing:-1px}
.brand-dot{width:14px;height:14px;border-radius:50%;background:var(--red)}
.nav{right:120px;top:48px;display:flex;gap:32px;font-size:17px;color:#555}
.searchbar{left:0;top:120px;width:1200px;height:50px;background:var(--charcoal);color:#fff}
.search-label{left:119px;top:14px;font-size:18px}
.search-input{left:184px;top:12px;width:220px;height:26px;background:#fff}
.search-go{left:409px;top:12px;width:26px;height:26px;background:var(--red);color:#fff;font-weight:700;text-align:center;line-height:25px;font-size:14px}
.signin{left:949px;top:17px;font-size:15px}
.divider{left:1008px;top:16px;width:1px;height:18px;background:#999}
.flag{top:18px;width:22px;height:14px}
.hero{left:0;top:170px;width:1200px;height:360px;background:linear-gradient(180deg,#4b8ed6 0%,#8fbce8 45%,#cfe2f3 75%,#7eaee2 100%)}
.hero h1{position:absolute;left:118px;top:110px;font-weight:400;font-size:48px;line-height:55px;color:#fff;letter-spacing:-1px}
.hero h1 span{color:var(--navy)}
.watch{left:121px;top:239px;height:36px;padding:0 14px 0 10px;background:var(--red);color:#fff;font-size:16px;font-weight:700;display:flex;align-items:center;gap:12px}
.quote{left:720px;top:117px;width:360px;height:155px;background:rgba(255,255,255,.3);padding:22px 22px 0;font-style:italic;font-size:15px;line-height:22.5px;color:var(--navy);text-align:right;white-space:nowrap}
.quote cite{font-style:normal;display:block}
.hero-rule{left:120px;top:532px;width:960px;height:8px;background:var(--charcoal)}
.tagline{left:100px;top:575px;width:1000px;text-align:center;font-size:20px;line-height:28px;color:var(--heading)}
.rule{left:120px;width:960px;height:1px;background:var(--rule)}
.intro{left:119px;top:700px;width:630px;font-size:15px;line-height:24px}
.solution{left:780px;width:300px;height:50px;display:flex;color:#fff;font-size:20px}
.solution .arrow{width:40px;background:var(--red);text-align:center;line-height:50px;font-weight:700}
.solution .label{flex:1;padding-left:14px;line-height:50px}
.solution b{font-weight:700}
.perf{top:703px;background:var(--red-dark)}
.sust{top:768px;background:var(--charcoal)}
.links{left:119px;top:887px;font-size:15px}
.links a{color:var(--red);text-decoration:none}
.footer{left:0;top:940px;width:1200px;height:60px;background:var(--footer);font-size:13px;color:#666}
.footer .addr{position:absolute;left:117px;top:32px;line-height:18px}
.follow{position:absolute;left:910px;top:43px}
.social{position:absolute;top:38px;width:23px;height:23px;background:#666}
.modal{left:240px;top:220px;width:710px;height:430px;background:rgba(120,120,128,.9);border-radius:8px}
.close{left:682px;top:10px;width:18px;height:18px;border-radius:50%;background:#ddd;color:#777;font-size:12px;font-weight:700;text-align:center;line-height:18px}
.screen{left:35px;top:25px;width:640px;height:360px;background:#020818}
.controls{left:35px;top:385px;width:640px;height:25px;background:linear-gradient(#f2f2f2,#c9c9c9);font-size:11px;color:#222}
.ctl-sep{position:absolute;top:0;width:1px;height:25px;background:#aaa}
.track{position:absolute;left:48px;top:10px;width:460px;height:5px;background:#ddd;border:1px solid #aaa;border-radius:3px}
.track-buffer{position:absolute;left:0;top:0;width:268px;height:3px;background:#999}
.thumb{position:absolute;left:59px;top:7px;width:12px;height:12px;background:#555;border-radius:2px}
.time{position:absolute;left:518px;top:7px}
</style>
</head>
<body>
<div class="abs top-strip"></div>

<header class="abs header">
  <div class="abs brand"><span>Lantern</span><span class="brand-dot"></span></div>
  <nav class="abs nav"><span>Home</span><span>Who we are</span><span>Cross the Lantern</span><span>Performance Solutions</span><span>Sustain Solutions</span></nav>
</header>

<div class="abs searchbar">
  <span class="abs search-label">Search</span>
  <span class="abs search-input"></span>
  <span class="abs search-go">›</span>
  <span class="abs signin">Sign In</span>
  <span class="abs divider"></span>
  <svg class="abs flag" style="left:1026px" viewBox="0 0 22 14"><rect width="22" height="14" fill="#1f3d8a"/><path d="M0 0L22 14M22 0L0 14" stroke="#fff" stroke-width="3"/><path d="M11 0V14M0 7H22" stroke="#fff" stroke-width="4"/><path d="M11 0V14M0 7H22" stroke="#d0202a" stroke-width="2"/></svg>
  <svg class="abs flag" style="left:1058px" viewBox="0 0 22 14"><rect width="7.3" height="14" fill="#1f3d8a"/><rect x="7.3" width="7.4" height="14" fill="#fff"/><rect x="14.7" width="7.3" height="14" fill="#d0202a"/></svg>
</div>

<section class="abs hero" role="img" aria-label="Photograph of a bridge deck seen from below against a blue sky with clouds">
  <h1>Hello and welcome to<br><span>Lantern Performance</span></h1>
  <div class="abs watch">
    <svg width="30" height="18" viewBox="0 0 30 18"><rect x="1" y="2" width="20" height="14" rx="2" fill="none" stroke="#fff" stroke-width="2"/><path d="M21 9L29 3V15Z" fill="#fff"/><circle cx="8" cy="11" r="2" fill="#fff"/><circle cx="14" cy="11" r="2" fill="#fff"/></svg>
    Watch our video
  </div>
  <blockquote class="abs quote">“We have become managers so preoccupied<br>with our digital messages that they<br>rarely look up from their screens to see<br>what is happening in the nondigital<br><cite>Marten Hollowell</cite></blockquote>
</section>
<div class="abs hero-rule"></div>

<p class="abs tagline">Lantern Performance Group is a team of certified consultants, trainers and subject matter<br>experts serving clients across North America, Europe and Asia Pacific</p>
<div class="abs rule" style="top:665px"></div>

<p class="abs intro">Lantern Performance Group Inc. is the leading provider of profit generating and people development solutions. With the hands-on experience of best practices, the state-of-the-art technology and in-depth information we help companies increase their efficiencies and profits. Frank, honest, committed, valuable and rewarding are words that customers use to describe the quality services provided by Lantern Performance Group.</p>

<div class="abs solution perf"><span class="arrow">›</span><span class="label"><b>Performance</b> Solutions</span></div>
<div class="abs solution sust"><span class="arrow">›</span><span class="label"><b>Sustain</b> Solutions</span></div>

<div class="abs rule" style="top:855px"></div>
<p class="abs links"><a>Learn more about us</a>, or find the right <a>solutions</a> for your specific business. We will be delighted to help you achieve better business results.</p>

<footer class="abs footer">
  <p class="addr"><b>Lantern Performance Group .</b> 27 Harbourview Rd . Alderport . NB E2K 5T1 . Canada<br><b>Telephone :</b>+1 800 555 0142 . <b>Email:</b>info@lantern-outcomes.com</p>
  <span class="follow">Follow us on</span>
  <span class="social" style="left:997px"></span>
  <span class="social" style="left:1027px"></span>
  <span class="social" style="left:1057px"></span>
</footer>

<div class="abs modal">
  <span class="abs close">×</span>
  <div class="abs screen">
    <svg class="abs" style="left:286px;top:146px" width="70" height="70" viewBox="0 0 70 70"><circle cx="35" cy="35" r="33" fill="none" stroke="#fff" stroke-width="3"/><path d="M29 20L48 35L29 50Z" fill="#fff"/></svg>
  </div>
  <div class="abs controls">
    <svg class="abs" style="left:12px;top:7px" width="12" height="12" viewBox="0 0 12 12"><path d="M1 0L12 6L1 12Z" fill="#333"/></svg>
    <span class="ctl-sep" style="left:38px"></span>
    <div class="track"><div class="track-buffer"></div></div>
    <span class="thumb"></span>
    <span class="time">0:04 / 2:32</span>
    <span class="ctl-sep" style="left:578px"></span>
    <svg class="abs" style="left:586px;top:7px" width="14" height="11" viewBox="0 0 14 11"><rect x="0.5" y="0.5" width="13" height="10" fill="none" stroke="#333"/><rect x="3" y="4" width="8" height="5" fill="#333"/></svg>
    <span class="ctl-sep" style="left:610px"></span>
    <svg class="abs" style="left:616px;top:7px" width="14" height="12" viewBox="0 0 14 12"><path d="M0 4H3L7 0V12L3 8H0Z" fill="#333"/><path d="M9 3Q11 6 9 9" stroke="#333" fill="none"/></svg>
  </div>
</div>
</body>
</html>
```